Web Application Graphic Design Project

We need a design for an online literacy application. The target audience are 9-12 year old children and the application will teach them literacy skills, like essay writing. It is a web-based application called Brivolen and the software developers now need a graphic design to implement into the code - no coding required, just design of the layout.
Wireframes are attached to give an overview of what the functionalities are - it runs in any ordinary web-browser (indicated in the wireframes as well). The application consists of a static background (workspace) onto which individual boxes are added as the student progresses through the tasks. A task panel on the left hand side allows the user to select a task, upon which a popup window will slide open on the right where they enter content. This content is then displayed on the workspace in the background in a box (which can be moved around to organise, seen in frame 3 ). Additional icons on left and right lead to new tasks.
Updates
The wireframe mockup of the application has been updated - please ignore the previous one, which has now been deleted. This is the final version to work from.
Reason: Would like to give more time to allow for a design that meets the young children target audience and for more creative ways for icons and colour schemes.
Reason: We are waiting for some further submissions to come through.
Target Market(s)
9-12 year old school children, so the design should be appealing to both boys and girls.
Industry/Entity Type
Graphic Design
Look and feel
Each slider illustrates characteristics of the customer's brand and the style your logo design should communicate.

```html
<!DOCTYPE html>
<html lang="en">
<head>
<meta charset="utf-8">
<title>Brivolen – Essay Writing</title>
<link rel="stylesheet" href="https://fonts.googleapis.com/css2?family=Source+Sans+3:wght@400;600;700&display=swap">
<style>
:root{
  --bar-green:#2f6f5c;
  --wood:#f0a63a;
  --paper:#fbf3b0;
  --paper-line:#c7cfd6;
  --margin-red:#e6b7a0;
  --board:#2a7a5a;
  --board-dark:#1e4d3b;
  --board-frame:#163b2e;
  --chalk:#ffffff;
  --chalk-done:#f3a530;
  --navy:#1b2d52;
  --ink:#2a2f3a;
  --card-line:#aebee0;
  --card-red:#d9342b;
  --icon:#1f2c4e;
  --pink:#c0246c;
  --lime:#a6c93a;
  --orange:#f3a530;
  --font:"Source Sans 3",Arial,sans-serif;
}
*{box-sizing:border-box;margin:0;padding:0}
html,body{width:1200px;height:927px;overflow:hidden}
body{font-family:var(--font);background:var(--paper)}
.app{position:relative;width:1200px;height:927px;overflow:hidden;
  background:
    linear-gradient(90deg,transparent 174px,var(--margin-red) 174px,var(--margin-red) 176px,transparent 176px,transparent 186px,var(--margin-red) 186px,var(--margin-red) 188px,transparent 188px),
    repeating-linear-gradient(180deg,transparent 0,transparent 29px,var(--paper-line) 29px,var(--paper-line) 31px) 0 150px/100% 100% no-repeat,
    var(--paper);}
.browser-bar{position:absolute;left:0;top:0;width:1200px;height:145px;background:var(--bar-green);border-bottom:12px solid var(--wood)}
.site-title{position:absolute;top:26px;width:100%;text-align:center;color:#fff;font-size:20px}
.nav-btn{position:absolute;top:58px;width:60px;height:52px}
.url-field{position:absolute;left:376px;top:58px;width:604px;height:48px;background:#f4f4f4;border-radius:4px}
.search-field{position:absolute;left:995px;top:58px;width:184px;height:48px;background:#f4f4f4;border-radius:14px}
.search-field svg{position:absolute;left:10px;top:7px}
.tool{position:absolute;width:110px;text-align:center;color:var(--ink);font-size:20px;line-height:1;z-index:3}
.tool svg{display:block;margin:0 auto 6px}
.task-board{position:absolute;left:106px;top:170px;width:271px;height:701px;background:var(--board-frame);border-top:12px solid var(--wood);border-bottom:14px solid var(--wood)}
.levels{position:absolute;left:0;top:0;width:100%;height:110px;background:var(--board-dark);display:flex;justify-content:space-around;padding-top:14px}
.level{text-align:center;font-size:21px}
.level .figure{width:50px;height:50px;border-radius:50%;margin:0 auto 6px}
.level.newbie{color:var(--pink)}.level.newbie .figure{background:var(--pink)}
.level.developer{color:var(--lime)}.level.developer .figure{background:var(--lime)}
.level.star{color:var(--orange)}.level.star .figure{background:var(--orange)}
.board{position:absolute;left:8px;top:118px;width:255px;height:500px;background:radial-gradient(ellipse at 45% 35%,#3a8c6a,var(--board) 60%,#216149)}
.board-ledge{position:absolute;left:0;bottom:0;width:100%;height:63px;background:linear-gradient(#1b4a38,#153a2c)}
.board h2{margin:14px 0 6px 18px;color:var(--chalk);font-size:20px;letter-spacing:6px;font-weight:700}
.board ul{list-style:none;margin-left:18px}
.board li{position:relative;height:27px;color:var(--chalk);font-size:19px;line-height:27px}
.board li.done{color:var(--chalk-done)}
.board li.done svg{position:absolute;left:208px;top:3px}
.card{position:absolute;background:#fff repeating-linear-gradient(180deg,transparent 0,transparent 14px,var(--card-line) 14px,var(--card-line) 15px);box-shadow:2px 3px 6px rgba(0,0,0,.25)}
.card::before{content:"";position:absolute;left:41px;top:0;bottom:0;width:2px;background:var(--card-red)}
.card .hole{position:absolute;left:13px;width:12px;height:12px;border-radius:50%;background:#e8e4cf;border:1px solid #b9b39a}
.card h3{position:absolute;left:60px;font-weight:400;color:var(--card-red);font-size:17px;white-space:nowrap}
.card p{position:absolute;left:60px;color:var(--ink);font-size:17px;line-height:31.5px}
.card-question{left:395px;top:183px;width:334px;height:203px}
.card-question .hole{top:41px}.card-question h3{top:35px}.card-question p{top:85px;width:270px}
.card-decode{left:501px;top:362px;width:334px;height:206px;overflow:hidden}
.card-decode .hole{top:41px}.card-decode h3{top:32px}.card-decode p{top:95px;line-height:22px;font-size:17px;width:260px}
.reference{position:absolute;left:723px;top:341px;width:330px;height:523px;box-shadow:2px 4px 8px rgba(0,0,0,.3);z-index:2}
.reference-head{height:110px;background:var(--navy);text-align:center;color:#fff;font-size:16px;padding-top:22px}
.reference-head .close{position:absolute;right:8px;top:6px}
.ref-search{margin:10px auto 0;width:162px;height:34px;background:#f0f0f0;border-radius:14px;text-align:left;color:#9aa0a8;font-size:16px;line-height:34px;padding-left:30px;position:relative}
.ref-search svg{position:absolute;left:8px;top:8px}
.pointer{position:absolute;left:995px;top:288px;z-index:1}
.reference-body{position:relative;height:413px;background:#fff repeating-linear-gradient(180deg,transparent 0,transparent 14px,var(--card-line) 14px,var(--card-line) 15px)}
.reference-body::before{content:"";position:absolute;left:41px;top:0;bottom:0;width:2px;background:var(--card-red)}
.reference-body .hole{position:absolute;left:10px;top:30px;width:12px;height:12px;border-radius:50%;background:#e8e4cf;border:1px solid #b9b39a}
.ref-list{list-style:none;position:absolute;left:53px;top:30px}
.ref-list li{height:30.3px;font-size:17px;color:var(--ink);display:flex;align-items:center;gap:8px}
.scroll{position:absolute;left:301px;top:20px;width:21px;height:367px;background:#e2e4ea;border-radius:10px}
.scroll i{position:absolute;left:4px;width:13px;height:13px;border-radius:50%;background:var(--navy)}
.scroll .thumb{position:absolute;left:5px;top:40px;width:11px;height:36px;background:var(--navy);border-radius:6px}
.brand{position:absolute;left:898px;top:160px;font-size:38px;font-weight:700;color:var(--pink);letter-spacing:1px}
</style>
</head>
<body>
<div class="app">

  <header class="browser-bar">
    <div class="site-title">Brivolen.com.au Copiright 2012</div>
    <svg class="nav-btn" style="left:10px" viewBox="0 0 60 52"><path d="M4 26 26 6v13h30v14H26v13z" fill="#fff"/></svg>
    <svg class="nav-btn" style="left:98px" viewBox="0 0 60 52"><path d="M56 26 34 6v13H4v14h30v13z" fill="#fff"/></svg>
    <svg class="nav-btn" style="left:186px" viewBox="0 0 60 52"><path d="M8 10l8-8 14 14L44 2l8 8-14 14 14 14-8 8-14-14-14 14-8-8 14-14z" fill="#fff"/></svg>
    <svg class="nav-btn" style="left:272px;width:70px" viewBox="0 0 70 52"><path d="M35 2 2 30h9v20h18V36h12v14h18V30h9z" fill="#fff"/></svg>
    <div class="url-field"></div>
    <div class="search-field"><svg width="36" height="36" viewBox="0 0 36 36"><circle cx="14" cy="14" r="10" fill="none" stroke="var(--bar-green)" stroke-width="4"/><path d="M21 21l11 11" stroke="var(--bar-green)" stroke-width="6" stroke-linecap="round"/></svg></div>
  </header>

  <nav>
    <div class="tool" style="left:6px;top:215px"><svg width="46" height="46" viewBox="0 0 46 46"><path d="M8 38l4-12L34 4l8 8-22 22z" fill="var(--icon)"/><path d="M4 44h38" stroke="var(--icon)" stroke-width="2"/></svg>Lesson</div>
    <div class="tool" style="left:3px;top:303px"><svg width="34" height="60" viewBox="0 0 34 60"><rect x="2" y="2" width="30" height="56" fill="none" stroke="var(--icon)" stroke-width="3"/><path d="M2 20h30M2 39h30" stroke="var(--icon)" stroke-width="3"/><path d="M13 11h8M13 30h8M13 49h8" stroke="var(--icon)" stroke-width="3"/></svg>Activities</div>
  </nav>

  <aside class="task-board">
    <div class="levels">
      <div class="level newbie"><div class="figure" role="img" aria-label="Teddy bear character"></div>Newbie</div>
      <div class="level developer"><div class="figure" role="img" aria-label="Reading child character"></div>Developer</div>
      <div class="level star"><div class="figure" role="img" aria-label="Graduate character"></div>Star</div>
    </div>
    <div class="board">
      <h2>ESSAY WRITING</h2>
      <ul>
        <li>Overview</li>
        <li class="done">The Question<svg width="22" height="22" viewBox="0 0 22 22"><rect x="1" y="4" width="17" height="17" fill="none" stroke="var(--chalk-done)" stroke-width="2"/><path d="M5 11l4 5 11-14" fill="none" stroke="var(--chalk-done)" stroke-width="3"/></svg></li>
        <li class="done">Decoding the Q<svg width="22" height="22" viewBox="0 0 22 22"><rect x="1" y="4" width="17" height="17" fill="none" stroke="var(--chalk-done)" stroke-width="2"/><path d="M5 11l4 5 11-14" fill="none" stroke="var(--chalk-done)" stroke-width="3"/></svg></li>
        <li class="done">Your Ideas<svg width="22" height="22" viewBox="0 0 22 22"><rect x="1" y="4" width="17" height="17" fill="none" stroke="var(--chalk-done)" stroke-width="2"/><path d="M5 11l4 5 11-14" fill="none" stroke="var(--chalk-done)" stroke-width="3"/></svg></li>
        <li>Structure</li>
        <li>Writing</li>
        <li>Review</li>
      </ul>
      <div class="board-ledge"></div>
    </div>
  </aside>

  <section class="card card-question">
    <span class="hole"></span>
    <h3>Teacher-Set Question</h3>
    <p>How has the internet changed our perception of the nature of information?</p>
  </section>

  <section class="card card-decode">
    <span class="hole"></span>
    <h3>Decoding The Question</h3>
    <p>Opinion - How?<br>Research Perceptions<br>Facts Information</p>
  </section>

  <div class="brand">Brivolen</div>

  <svg class="pointer" width="115" height="58" viewBox="0 0 115 58"><path d="M5 58 105 0 38 58z" fill="var(--navy)"/></svg>

  <section class="reference">
    <div class="reference-head">
      REFERENCE
      <svg class="close" width="26" height="26" viewBox="0 0 26 26"><path d="M4 4l18 18M22 4 4 22" stroke="#fff" stroke-width="5"/></svg>
      <div class="ref-search"><svg width="18" height="18" viewBox="0 0 18 18"><circle cx="7" cy="7" r="5" fill="none" stroke="#9aa0a8" stroke-width="2"/><path d="M11 11l5 5" stroke="#9aa0a8" stroke-width="3"/></svg>Search</div>
    </div>
    <div class="reference-body">
      <span class="hole"></span>
      <ul class="ref-list">
        <li><svg width="16" height="20" viewBox="0 0 16 20"><path d="M1 1h10l4 4v14H1z" fill="none" stroke="var(--navy)" stroke-width="2"/><path d="M4 8h8M4 11h8M4 14h8" stroke="var(--navy)" stroke-width="1.5"/></svg>Apostrophe</li>
        <li><svg width="16" height="20" viewBox="0 0 16 20"><path d="M1 1h10l4 4v14H1z" fill="none" stroke="var(--navy)" stroke-width="2"/><path d="M4 8h8M4 11h8M4 14h8" stroke="var(--navy)" stroke-width="1.5"/></svg>Argument</li>
        <li><svg width="16" height="20" viewBox="0 0 16 20"><path d="M1 1h10l4 4v14H1z" fill="none" stroke="var(--navy)" stroke-width="2"/><path d="M4 8h8M4 11h8M4 14h8" stroke="var(--navy)" stroke-width="1.5"/></svg>Clause</li>
        <li><svg width="16" height="20" viewBox="0 0 16 20"><path d="M1 1h10l4 4v14H1z" fill="none" stroke="var(--navy)" stroke-width="2"/><path d="M4 8h8M4 11h8M4 14h8" stroke="var(--navy)" stroke-width="1.5"/></svg>Comma</li>
        <li><svg width="16" height="20" viewBox="0 0 16 20"><path d="M1 1h10l4 4v14H1z" fill="none" stroke="var(--navy)" stroke-width="2"/><path d="M4 8h8M4 11h8M4 14h8" stroke="var(--navy)" stroke-width="1.5"/></svg>Essay</li>
        <li><svg width="16" height="20" viewBox="0 0 16 20"><path d="M1 1h10l4 4v14H1z" fill="none" stroke="var(--navy)" stroke-width="2"/><path d="M4 8h8M4 11h8M4 14h8" stroke="var(--navy)" stroke-width="1.5"/></svg>Full Stop</li>
        <li><svg width="16" height="20" viewBox="0 0 16 20"><path d="M1 1h10l4 4v14H1z" fill="none" stroke="var(--navy)" stroke-width="2"/><path d="M4 8h8M4 11h8M4 14h8" stroke="var(--navy)" stroke-width="1.5"/></svg>Introduction</li>
        <li><svg width="16" height="20" viewBox="0 0 16 20"><path d="M1 1h10l4 4v14H1z" fill="none" stroke="var(--navy)" stroke-width="2"/><path d="M4 8h8M4 11h8M4 14h8" stroke="var(--navy)" stroke-width="1.5"/></svg>Noun</li>
        <li><svg width="16" height="20" viewBox="0 0 16 20"><path d="M1 1h10l4 4v14H1z" fill="none" stroke="var(--navy)" stroke-width="2"/><path d="M4 8h8M4 11h8M4 14h8" stroke="var(--navy)" stroke-width="1.5"/></svg>Orientation</li>
        <li><svg width="16" height="20" viewBox="0 0 16 20"><path d="M1 1h10l4 4v14H1z" fill="none" stroke="var(--navy)" stroke-width="2"/><path d="M4 8h8M4 11h8M4 14h8" stroke="var(--navy)" stroke-width="1.5"/></svg>Sentence</li>
        <li><svg width="16" height="20" viewBox="0 0 16 20"><path d="M1 1h10l4 4v14H1z" fill="none" stroke="var(--navy)" stroke-width="2"/><path d="M4 8h8M4 11h8M4 14h8" stroke="var(--navy)" stroke-width="1.5"/></svg>Topic Sentence</li>
        <li><svg width="16" height="20" viewBox="0 0 16 20"><path d="M1 1h10l4 4v14H1z" fill="none" stroke="var(--navy)" stroke-width="2"/><path d="M4 8h8M4 11h8M4 14h8" stroke="var(--navy)" stroke-width="1.5"/></svg>Paragraph</li>
      </ul>
      <div class="scroll"><i style="top:4px"></i><span class="thumb"></span><i style="bottom:4px"></i></div>
    </div>
  </section>

  <nav>
    <div class="tool" style="left:1069px;top:158px"><svg width="28" height="50" viewBox="0 0 28 50"><circle cx="14" cy="7" r="6" fill="var(--icon)"/><path d="M4 16h20v16h-4v16h-5V34h-2v14H8V32H4z" fill="var(--icon)"/></svg>Name</div>
    <div class="tool" style="left:1069px;top:250px"><svg width="40" height="48" viewBox="0 0 40 48"><path d="M4 10 14 4v30L4 40z" fill="var(--icon)"/><path d="M10 6 20 2v30l-10 6z" fill="none" stroke="var(--icon)" stroke-width="2"/><rect x="14" y="22" width="24" height="24" fill="var(--icon)"/><rect x="30" y="30" width="6" height="6" fill="#fff"/></svg>Reference</div>
    <div class="tool" style="left:1069px;top:348px"><svg width="40" height="52" viewBox="0 0 40 52"><path d="M2 2h26l10 10v38H2z" fill="none" stroke="var(--icon)" stroke-width="3"/><path d="M8 18h24M8 26h24M8 34h24M8 42h24" stroke="var(--icon)" stroke-width="3"/></svg>Samples</div>
    <div class="tool" style="left:1069px;top:442px"><svg width="42" height="42" viewBox="0 0 42 42"><rect x="2" y="2" width="38" height="38" rx="3" fill="none" stroke="var(--icon)" stroke-width="3"/><rect x="10" y="2" width="22" height="14" fill="var(--icon)"/><rect x="10" y="24" width="22" height="16" fill="none" stroke="var(--icon)" stroke-width="3"/></svg>Save</div>
    <div class="tool" style="left:1069px;top:527px"><svg width="54" height="50" viewBox="0 0 54 50"><g fill="none" stroke="var(--icon)" stroke-width="3"><rect x="2" y="2" width="50" height="12" rx="6"/><rect x="2" y="19" width="50" height="12" rx="6"/><rect x="2" y="36" width="50" height="12" rx="6"/></g><circle cx="40" cy="8" r="6" fill="var(--icon)"/><circle cx="30" cy="25" r="6" fill="var(--icon)"/><circle cx="10" cy="42" r="6" fill="var(--icon)"/></svg>Settings</div>
    <div class="tool" style="left:1069px;top:616px"><svg width="42" height="62" viewBox="0 0 42 62"><rect x="2" y="2" width="38" height="58" fill="none" stroke="var(--icon)" stroke-width="3"/><path d="M6 4l22 8v48L6 58z" fill="var(--icon)"/></svg>Exit</div>
  </nav>

</div>
</body>
</html>
```